Flyer for Velvet Lark Concert

8.5x11 color flyer, to get people to attend excellent concert

Requirements
Should not have
• I don't like a lot of musical symbols incorporated into the design.

```html
<!DOCTYPE html>
<html lang="en">
<head>
<meta charset="utf-8">
<title>War &amp; Peace — Velvet Lark Concert</title>
<link href="https://fonts.googleapis.com/css2?family=Cinzel:wght@500;600&family=Libre+Baskerville:wght@400;700&family=Open+Sans:ital,wght@0,400;0,600;0,700;1,400&display=swap" rel="stylesheet">
<style>
  :root {
    --crimson: #8a0b3c;
    --purple: #46206e;
    --cream: #f6e0b2;
    --cream-soft: #fdf3e1;
    --ink: #1d1b22;
    --gold: #f1d79c;
    --page: #ececec;
    --white: #ffffff;
  }
  * { box-sizing: border-box; margin: 0; padding: 0; }
  html, body { width: 1200px; height: 1200px; overflow: hidden; background: var(--page); }
  body { position: relative; font-family: "Open Sans", Arial, sans-serif; color: var(--ink); }

  .flyer {
    position: absolute; left: 233px; top: 107px;
    width: 735px; height: 951px;
    background: var(--white); overflow: hidden;
  }
  .flyer > * { position: absolute; }

  .backdrop { left: 0; top: 0; width: 735px; height: 951px; }

  .top-band { left: 0; top: 0; width: 735px; height: 83px; background: var(--crimson); }
  .crest-ornament {
    left: 252px; top: 15px; width: 232px; height: 52px; border-radius: 26px;
    background: linear-gradient(90deg, rgba(241,215,156,0.15), rgba(241,215,156,0.55), rgba(241,215,156,0.15));
  }

  .presenter { left: 0; top: 101px; width: 735px; text-align: center; color: var(--purple); }
  .presenter-name { font-family: "Libre Baskerville", Georgia, serif; font-weight: 700; font-size: 21.5px; letter-spacing: 0.2px; }
  .presenter-staff { font-weight: 700; font-size: 15.5px; margin-top: 1px; }
  .presenter-verb { font-weight: 700; font-size: 12.5px; letter-spacing: 6px; margin-top: 9px; }

  .title { left: 30px; top: 178px; font-family: "Cinzel", "Times New Roman", serif; font-weight: 600; line-height: 1; }
  .title-war { display: block; color: var(--purple); font-size: 104px; letter-spacing: -2px; }
  .title-amp { font-size: 58px; }
  .title-peace { display: block; color: var(--crimson); font-size: 104px; letter-spacing: -1px; margin-top: 2px; }

  .show-date {
    left: 440px; width: 262px; height: 60px;
    background: var(--cream); border-radius: 30px 4px 30px 4px;
    text-align: center; padding-top: 4px;
  }
  .show-date.saturday { top: 195px; }
  .show-date.sunday { top: 268px; }
  .show-day { color: var(--crimson); font-weight: 600; font-size: 24px; line-height: 1.05; }
  .show-time { font-weight: 600; font-size: 19.5px; line-height: 1.1; }

  .venue { left: 430px; top: 337px; width: 280px; text-align: center; color: var(--purple); font-weight: 700; font-size: 14.5px; line-height: 1.25; }

  .choir-photo {
    left: 34px; top: 408px; width: 478px; height: 253px;
    background: linear-gradient(180deg, #e9c15e 0%, #d8aa52 45%, #8d6c4b 75%, #c7ab8c 100%);
  }

  .invite { left: 520px; top: 406px; width: 182px; text-align: right; }
  .invite-head { color: var(--crimson); font-weight: 700; font-size: 16.5px; line-height: 1.15; }
  .invite-body { font-size: 15px; line-height: 1.27; margin-top: 4px; }
  .invite-head.featuring { margin-top: 10px; }

  .tickets {
    left: 35px; top: 686px; width: 260px; height: 62px;
    background: var(--cream); border-radius: 30px 4px 30px 4px;
    text-align: center; padding-top: 4px;
    color: var(--crimson); font-weight: 700; font-size: 16px; line-height: 1.15;
  }
  .prices { left: 337px; top: 687px; font-weight: 700; font-size: 15px; color: var(--purple); border-collapse: collapse; }
  .prices td { padding: 0; line-height: 20.5px; }
  .prices td.amount { padding-left: 42px; }

  .childcare { left: 40px; top: 761px; width: 460px; text-align: center; font-size: 12.5px; }

  .director-portrait {
    left: 592px; top: 686px; width: 110px; height: 169px;
    background: linear-gradient(180deg, #d8d2e0 0%, #a99bbd 55%, #4a3a62 100%);
  }
  .director-caption { left: 560px; top: 858px; width: 142px; text-align: right; color: var(--gold); font-size: 12.5px; line-height: 1.2; }
  .director-caption em { font-style: italic; }

  .choir-name {
    left: 85px; top: 818px; display: flex; align-items: center; gap: 12px;
    font-family: "Libre Baskerville", Georgia, serif; font-weight: 400; font-size: 40px; color: var(--purple); letter-spacing: 1px;
  }
  .choir-name-dot { width: 20px; height: 20px; border-radius: 50%; background: var(--purple); }

  .footer-band { left: 0; top: 893px; width: 735px; height: 58px; background: var(--purple); }
  .web { left: 0; top: 908px; width: 735px; text-align: center; color: var(--gold); font-weight: 700; font-size: 16.5px; }
  .scroll-ornament { top: 905px; width: 20px; height: 34px; border-radius: 10px; background: rgba(241,215,156,0.5); }
  .scroll-ornament.left { left: 212px; }
  .scroll-ornament.right { left: 502px; }
</style>
</head>
<body>
<main class="flyer">
  <svg class="backdrop" viewBox="0 0 735 951" aria-hidden="true">
    <path d="M0 83 H300 C170 120 60 200 0 330 Z" fill="var(--cream)"/>
    <rect x="0" y="795" width="735" height="100" fill="var(--cream-soft)"/>
    <path d="M735 678 C700 800 640 870 520 895 L735 895 Z" fill="var(--purple)"/>
  </svg>

  <div class="top-band"></div>
  <div class="crest-ornament" role="img" aria-label="Gold flourish ornament"></div>

  <header class="presenter">
    <p class="presenter-name">VELVET LARK: CHORAL ARTISTS OF THE MESA</p>
    <p class="presenter-staff">Adrian Vale, Artistic Director | Mirela Osten, Executive Director</p>
    <p class="presenter-verb">PRESENTS</p>
  </header>

  <h1 class="title">
    <span class="title-war">WAR<span class="title-amp">&amp;</span></span>
    <span class="title-peace">PEACE</span>
  </h1>

  <div class="show-date saturday">
    <p class="show-day">SATURDAY</p>
    <p class="show-time">October 13 at 7:30pm</p>
  </div>
  <div class="show-date sunday">
    <p class="show-day">SUNDAY</p>
    <p class="show-time">October 14 at 3:00pm</p>
  </div>
  <p class="venue">Cedar Hall Chapel<br>418 Juniper Lane NE Sandford</p>

  <div class="choir-photo" role="img" aria-label="Photo of the choir singing in black with a conductor at a grand piano"></div>

  <section class="invite">
    <h2 class="invite-head">JOIN THE SINGERS<br>OF VELVET LARK</h2>
    <p class="invite-body">as we perform music borne out of warfare and conflict, and music that celebrates peace and love.</p>
    <h2 class="invite-head featuring">FEATURING</h2>
    <p class="invite-body">music of<br>Tomas Rendell, Ilse Marrow, Owen Hale, Clara Penn, and others.</p>
  </section>

  <div class="tickets">TICKETS AVAILABLE<br>ONLINE &amp;<br>AT THE DOOR</div>
  <table class="prices">
    <tr><td>General</td><td class="amount">$20</td></tr>
    <tr><td>Seniors</td><td class="amount">$15</td></tr>
    <tr><td>Students</td><td class="amount">$10</td></tr>
  </table>
  <p class="childcare">Complimentary childcare provided at both performances.</p>

  <div class="director-portrait" role="img" aria-label="Portrait of the artistic director"></div>
  <p class="director-caption">Adrian Vale<br><em>Artistic Director</em></p>

  <div class="choir-name"><span class="choir-name-dot"></span>VELVET LARK</div>

  <div class="footer-band"></div>
  <div class="scroll-ornament left" role="img" aria-label="Small gold scroll ornament"></div>
  <p class="web">www.velvetlark-choir.org</p>
  <div class="scroll-ornament right" role="img" aria-label="Small gold scroll ornament"></div>
</main>
</body>
</html>
```